Kestrel Roofing & Restoration Business Card Design

Lookiing for a double sided business card design that will have rounded corners, will look good with Spot UV, Soft Laminate, or Gloss
Front of card should have Logo, Name and Contact Info, License numbers
Back of card should have Logo, maybe other small details

```html
<!DOCTYPE html>
<html lang="en">
<head>
<meta charset="utf-8">
<title>Kestrel Roofing &amp; Restoration — Business Card</title>
<link rel="stylesheet" href="https://fonts.googleapis.com/css2?family=Montserrat:wght@400;500;600&family=Poppins:wght@500&display=swap">
<style>
  :root {
    --backdrop: #c9c9c9;
    --card-dark: #222222;
    --card-light: #ffffff;
    --ink: #1f1f1f;
    --muted: #8a8a8a;
    --accent: #1aa3e0;
    --white: #ffffff;
  }
  * { margin: 0; padding: 0; box-sizing: border-box; }
  html, body {
    width: 1200px; height: 1200px; overflow: hidden;
    background: var(--backdrop);
  }
  .canvas { position: relative; width: 1200px; height: 1200px; }

  .card {
    position: absolute;
    width: 838px; height: 478px;
    border-radius: 38px;
    overflow: hidden;
  }
  .card--back { left: 194px; top: 70px; background: var(--card-dark); }
  .card--front { left: 192px; top: 624px; background: var(--card-light); }

  .brand {
    position: absolute;
    display: flex; align-items: center;
    font-family: "Poppins", sans-serif;
    font-weight: 500;
    text-transform: uppercase;
    line-height: 1.12;
  }
  .brand__square { flex: none; background: var(--accent); }
  .brand--large {
    left: 0; right: 0; top: 184px;
    justify-content: center; gap: 24px;
    color: var(--white); font-size: 38px;
  }
  .brand--large .brand__square { width: 44px; height: 44px; }
  .brand--small {
    left: 52px; top: 52px; gap: 16px;
    color: var(--ink); font-size: 27px;
  }
  .brand--small .brand__square { width: 30px; height: 30px; }

  .person {
    position: absolute; left: 51px; top: 250px; right: 68px;
    font-family: "Montserrat", sans-serif;
  }
  .person__name { font-weight: 600; font-size: 29px; color: var(--ink); }
  .person__role {
    display: flex; align-items: flex-end; gap: 8px;
    margin-top: 6px;
    font-size: 23px; font-weight: 400; color: var(--muted);
  }
  .person__rule { flex: 1; height: 3px; background: var(--accent); margin-bottom: 6px; }

  .contacts {
    position: absolute; left: 50px; top: 350px;
    list-style: none;
    font-family: "Montserrat", sans-serif;
    font-size: 23px; font-weight: 500; color: var(--ink);
  }
  .contacts li { display: flex; align-items: center; gap: 12px; height: 35.5px; }
  .contacts svg { width: 26px; height: 26px; flex: none; }
  .contacts .highlight { color: var(--accent); }

  .address {
    position: absolute; right: 58px; top: 388px;
    text-align: right;
    font-family: "Montserrat", sans-serif;
    font-size: 23px; font-weight: 500; color: var(--ink);
    line-height: 35.5px;
    font-style: normal;
  }
</style>
</head>
<body>
<main class="canvas">

  <section class="card card--back" aria-label="Card back">
    <div class="brand brand--large">
      <span class="brand__square"></span>
      <span>Kestrel Roofing &amp;<br>Restoration</span>
    </div>
  </section>

  <section class="card card--front" aria-label="Card front">
    <div class="brand brand--small">
      <span class="brand__square"></span>
      <span>Kestrel Roofing &amp;<br>Restoration</span>
    </div>

    <div class="person">
      <p class="person__name">Name Surename</p>
      <p class="person__role"><span>Founder</span><span class="person__rule"></span></p>
    </div>

    <ul class="contacts">
      <li>
        <svg viewBox="0 0 24 24" fill="none" stroke="#1aa3e0" stroke-width="2" stroke-linecap="round" stroke-linejoin="round" aria-hidden="true">
          <path d="M5 3h3l2 5-2.5 1.5a11 11 0 0 0 7 7L16 14l5 2v3a2 2 0 0 1-2 2A17 17 0 0 1 3 5a2 2 0 0 1 2-2z"/>
          <path d="M15 3a6 6 0 0 1 6 6M15 7a2 2 0 0 1 2 2"/>
        </svg>
        <span>555-014-2286</span>
      </li>
      <li>
        <svg viewBox="0 0 24 24" aria-hidden="true">
          <rect x="2" y="5" width="20" height="14" rx="1" fill="#1aa3e0"/>
          <path d="M3 6l9 7 9-7" fill="none" stroke="#ffffff" stroke-width="1.6"/>
        </svg>
        <span>email@website.com</span>
      </li>
      <li>
        <svg viewBox="0 0 24 24" fill="none" stroke="#1aa3e0" stroke-width="1.8" aria-hidden="true">
          <circle cx="12" cy="12" r="9.5"/>
          <ellipse cx="12" cy="12" rx="4" ry="9.5"/>
          <path d="M2.5 12h19M4 7h16M4 17h16"/>
        </svg>
        <span>www.<span class="highlight">website</span>.com</span>
      </li>
    </ul>

    <address class="address">123 Anywhere St,<br>Any City, ST 12345</address>
  </section>

</main>
</body>
</html>
```